Product Sales Website Design - E-commerce - Shopify etc

We have been selling printing equipment for some time now and think that it will be useful to sell the products on the internet, using a simple e-commerce platform, such as shopify etc. There are roughly a few dozen products - so basically, the idea is to have a modern, simple and clean home page. When someone looks at it, they think, this is it - I want to buy here. I am not going to impose any ideas or say how I want it done.

Just so you know, at the moment there are three categories of products. One being printers, scanners and accessories.

I am excited by this whole project and don't want to have good designers backing out because they feel i am imposing restrictions. Feel free to impress me.

Industry/Entity Type

E-Commerce

Requirements
Must have
• integration with an e-commerce platform is a must or show how to integrate, so I can easily introduce further products.

```html
<!DOCTYPE html>
<html lang="en">
<head>
<meta charset="utf-8">
<title>Harlow Equipments</title>
<link href="https://fonts.googleapis.com/css2?family=Source+Sans+3:wght@400;600;700&display=swap" rel="stylesheet">
<style>
:root{
  --ink:#3a3a3a;
  --muted:#8a8a8a;
  --blue:#1a8fc2;
  --red:#b5302e;
  --red-dark:#8e2220;
  --panel:#f0f0f0;
  --card-bg:#ececec;
  --line:#dcdcdc;
  --btn:#7f7f7f;
  --footer:#262626;
  --footer-text:#e6e6e6;
  --page:#fbfbfb;
}
*{box-sizing:border-box;margin:0;padding:0}
html,body{width:708px;height:1200px;overflow:hidden}
body{position:relative;background:var(--page);font-family:"Source Sans 3",Arial,sans-serif;color:var(--ink)}
.abs{position:absolute}

/* header */
.site-header{position:absolute;left:0;top:0;width:708px;height:83px;background:linear-gradient(#ffffff,#f2f2f2)}
.brand-mark{left:77px;top:22px;width:34px;height:34px;border-radius:50%;background:#8c8c8c}
.brand-name{left:125px;top:18px;font-size:17px;line-height:21px;font-weight:400;letter-spacing:1px;color:#4a4a4a;text-transform:uppercase}
.cart{left:453px;top:13px}
.cart-text{left:482px;top:14px;font-size:7.5px;line-height:10px;color:#666}
.header-rule{left:390px;top:46px;width:240px;height:1px;background:var(--line)}
.call-label{right:78px;top:13px;font-size:7.5px;font-weight:700;color:#333}
.call-number{right:78px;top:24px;font-size:14px;color:var(--blue);letter-spacing:.3px}
.main-nav{left:321px;top:60px;display:flex;font-size:7.4px;color:#333;text-transform:uppercase}
.main-nav span{padding:0 8px;border-left:1px solid #777;line-height:8px}
.main-nav span:first-child{border:none;padding-left:0;color:#777;position:relative}
.main-nav span:first-child::after{content:"";position:absolute;left:9px;top:12px;border:3px solid transparent;border-bottom-color:#333}

/* hero */
.hero{left:0;top:83px;width:708px;height:227px;background:radial-gradient(ellipse at 55% 45%,#eaeaea,#cdcdcd)}
.hero-image{left:92px;top:25px;width:220px;height:180px;background:linear-gradient(160deg,#4b4f57,#2b2e33);border-radius:8px}
.hero-arrow{width:24px;height:24px;border-radius:50%;background:#fff;border:1px solid #bbb;display:flex;align-items:center;justify-content:center}
.hero-title{left:339px;top:36px;font-size:21px;line-height:29px;color:#555;font-weight:400}
.hero-title em{font-weight:600;font-style:italic}
.hero-copy{left:339px;top:111px;width:285px;font-size:7.4px;line-height:12px;color:#777}
.btn-buy{left:338px;top:164px;width:73px;height:24px;background:linear-gradient(var(--red),var(--red-dark));color:#fff;font-size:8.5px;font-weight:600;display:flex;align-items:center;justify-content:center;border-radius:2px}

/* categories */
.categories{left:77px;top:343px;width:129px;height:205px;background:var(--panel)}
.categories h3{position:absolute;left:9px;top:8px;font-size:13px;font-weight:400;color:#444}
.categories ul{position:absolute;left:8px;top:33px;width:113px;list-style:none}
.categories li{font-size:7.3px;color:#777;height:18.4px;line-height:18px;border-bottom:1px solid #e0e0e0;padding-left:12px;position:relative}
.categories li::before{content:"→";position:absolute;left:0;font-size:7px}

.section-title{font-size:13.5px;font-weight:400;color:#444}
.pager{width:14px;height:14px;border-radius:50%;background:#8a8a8a;display:flex;align-items:center;justify-content:center}

/* product cards */
.card{position:absolute;width:130px}
.card .thumb{width:130px;background:linear-gradient(#f4f4f4,#e6e6e6)}
.card .thumb::after{content:"";display:block;margin:auto;width:60%;height:65%;position:relative;top:18%;background:linear-gradient(#5a5d63,#2f3135);border-radius:4px}
.card h4{font-size:10px;font-weight:400;color:var(--blue);margin:14px 0 0 2px}
.card p{font-size:7.2px;line-height:10.4px;color:var(--muted);margin:6px 0 0 0}
.card .btn{display:inline-block;margin-top:10px;background:var(--btn);color:#fff;font-size:7.2px;padding:0 7px;line-height:18px}
.featured h4{text-transform:uppercase}
.featured .thumb{height:94px}
.new .thumb{height:76px}
.new h4{margin-top:12px}
.new p{margin-top:4px}
.new .btn{margin-top:11px}

/* welcome + news */
.welcome{left:78px;top:977px;width:410px}
.welcome h2{font-size:11px;font-weight:700;color:#333}
.welcome p{font-size:6.9px;line-height:10.8px;color:#666;margin-top:9px}
.welcome p+p{margin-top:11px}
.news{left:503px;top:975px;width:130px}
.news h2{font-size:10px;font-weight:600;color:#333;margin-left:3px}
.news-item{padding:12px 0 10px 0;border-bottom:1px solid #e2e2e2;font-size:7.2px;line-height:10.6px;color:#666}
.news-item:last-child{border:none;padding-top:6px}
.news-item time{display:block;color:var(--blue);margin-top:8px}

/* footer */
.site-footer{left:0;top:1120px;width:708px;height:80px;background:var(--footer)}
.footer-nav{left:78px;top:21px;display:flex;gap:18px;font-size:7px;color:var(--footer-text);text-transform:uppercase}
.copyright{left:78px;top:40px;font-size:7.2px;line-height:13px;color:var(--footer-text)}
.follow{right:78px;top:19px;font-size:11px;color:var(--footer-text)}
.socials{left:533px;top:43px;display:flex;gap:2px}
.socials span{width:18px;height:18px;border-radius:50%;background:#b8b8b8;border:1px solid #ddd}
</style>
</head>
<body>

<header class="site-header">
  <div class="abs brand-mark"></div>
  <div class="abs brand-name">Harlow<br>Equipments</div>
  <svg class="abs cart" width="20" height="18" viewBox="0 0 20 18"><path d="M1 2h3l2 9h10l2-7H5" fill="none" stroke="#444" stroke-width="1.6"/><circle cx="8" cy="15" r="1.6" fill="#444"/><circle cx="15" cy="15" r="1.6" fill="#444"/></svg>
  <div class="abs cart-text">My Cart (0)<br>Contain Item</div>
  <div class="abs header-rule"></div>
  <div class="abs call-label">CALL US NOW!</div>
  <div class="abs call-number">555.014.0199</div>
  <nav class="abs main-nav"><span>Home</span><span>About</span><span>Shop</span><span>Blog</span><span>Product</span><span>Support</span><span>Contact Us</span></nav>
</header>

<section class="abs hero">
  <div class="abs hero-image" role="img" aria-label="Dark grey inkjet printer with a blue accent stripe"></div>
  <div class="abs hero-arrow" style="left:46px;top:105px"><svg width="8" height="10"><path d="M6 1L2 5l4 4" fill="none" stroke="#333" stroke-width="2"/></svg></div>
  <div class="abs hero-arrow" style="left:638px;top:105px"><svg width="8" height="10"><path d="M2 1l4 4-4 4" fill="none" stroke="#333" stroke-width="2"/></svg></div>
  <h1 class="abs hero-title">Great with <em>copiers.</em><br>Even better with <em>people.</em></h1>
  <p class="abs hero-copy">Sed ut perspiciatis unde omnis iste natus error sit voluptatem accusantium doloremque laudantium, totam rem aperiam, eaque ipsa quae ab illo inventore veritatis quasi architecto beata</p>
  <div class="abs btn-buy">BUY NOW &gt;&gt;</div>
</section>

<aside class="abs categories">
  <h3>Categories</h3>
  <ul>
    <li>At vero eos et accusamus</li>
    <li>dignissimos ducimus</li>
    <li>qui blanditiis praesentium</li>
    <li>voluptatum deleniti</li>
    <li>atque corrupti quos</li>
    <li>dolores et quas molestias</li>
    <li>At vero eos et accusamus</li>
    <li>dignissimos ducimus</li>
    <li>qui blanditiis praesentium</li>
  </ul>
</aside>

<h2 class="abs section-title" style="left:219px;top:344px">Featured Products</h2>
<div class="abs pager" style="left:598px;top:347px"><svg width="6" height="8"><path d="M5 1L2 4l3 3" fill="none" stroke="#fff" stroke-width="1.6"/></svg></div>
<div class="abs pager" style="left:615px;top:347px"><svg width="6" height="8"><path d="M1 1l3 3-3 3" fill="none" stroke="#fff" stroke-width="1.6"/></svg></div>

<div class="featured">
  <div class="card" style="left:219px;top:372px"><div class="thumb" role="img" aria-label="Printer product photo"></div><h4>Printer</h4><p>At vero eos et accusamus et iustoese odio dignissimos ducim.</p><span class="btn">Buy Now !</span></div>
  <div class="card" style="left:360px;top:372px"><div class="thumb" role="img" aria-label="Scanner product photo"></div><h4>Scanners</h4><p>At vero eos et accusamus et iustoese odio dignissimos ducim.</p><span class="btn">Buy Now !</span></div>
  <div class="card" style="left:502px;top:372px"><div class="thumb" role="img" aria-label="Coloured ink cartridges photo"></div><h4>Accessories</h4><p>At vero eos et accusamus et iustoese odio dignissimos ducim.</p><span class="btn">Buy Now !</span></div>
</div>

<h2 class="abs section-title" style="left:78px;top:573px">New Products</h2>

<div class="new">
  <div class="card" style="left:77px;top:598px"><div class="thumb" role="img" aria-label="Inkjet printer photo"></div><h4>Product Name</h4><p>At vero eos et accusamus et iustoese odio dignissimos ducim.</p><span class="btn">Buy Now !</span></div>
  <div class="card" style="left:218px;top:598px"><div class="thumb" role="img" aria-label="Laser multifunction printer photo"></div><h4>Product Name</h4><p>At vero eos et accusamus et iustoese odio dignissimos ducim.</p><span class="btn">Buy Now !</span></div>
  <div class="card" style="left:360px;top:598px"><div class="thumb" role="img" aria-label="Office copier photo"></div><h4>Product Name</h4><p>At vero eos et accusamus et iustoese odio dignissimos ducim.</p><span class="btn">Buy Now !</span></div>
  <div class="card" style="left:502px;top:598px"><div class="thumb" role="img" aria-label="All-in-one printer photo"></div><h4>Product Name</h4><p>At vero eos et accusamus et iustoese odio dignissimos ducim.</p><span class="btn">Buy Now !</span></div>

  <div class="card" style="left:77px;top:775px"><div class="thumb" role="img" aria-label="Laser printer photo"></div><h4>Product Name</h4><p>At vero eos et accusamus et iustoese odio dignissimos ducim.</p><span class="btn">Buy Now !</span></div>
  <div class="card" style="left:218px;top:775px"><div class="thumb" role="img" aria-label="Colour laser printer photo"></div><h4>Product Name</h4><p>At vero eos et accusamus et iustoese odio dignissimos ducim.</p><span class="btn">Buy Now !</span></div>
  <div class="card" style="left:360px;top:775px"><div class="thumb" role="img" aria-label="Inkjet office printer photo"></div><h4>Product Name</h4><p>At vero eos et accusamus et iustoese odio dignissimos ducim.</p><span class="btn">Buy Now !</span></div>
  <div class="card" style="left:502px;top:775px"><div class="thumb" role="img" aria-label="Multifunction printer with photo print photo"></div><h4>Product Name</h4><p>At vero eos et accusamus et iustoese odio dignissimos ducim.</p><span class="btn">Buy Now !</span></div>
</div>

<section class="abs welcome">
  <h2>WELCOME TO Harlow Equipments..</h2>
  <p>At vero eos et accusamus et iusto odio dignissimos ducimus qui blanditiis praesentium voluptatum deleniti atque corrupti quos dolores et quas molestias excepturi sint occaecati cupiditate non provident, similique sunt in culpa qui officia deserunt mollitia animi, id est laborum et dolorum fuga.</p>
  <p>Et harum quidem rerum facilis est et expedita distinctio. Nam libero tempore, cum soluta nobis est eligendi optio cumque nihil impedit quo minus id quod maxime placeat facere possimus, omnis voluptas assumenda est, omnis dolor repellendus. Temporibus autem quibusdam et aut officiis debitis aut rerum necessitatibus saepe eveniet ut et voluptates repudiandae sint et molestiae non recusandae.</p>
</section>

<aside class="abs news">
  <h2>LATEST NEWS</h2>
  <div class="news-item">At vero eos et accusamus ducimus qui blanditiis praesentium.<time>25 Jan 2014</time></div>
  <div class="news-item">At vero eos et accusamus ducimus qui blanditiis praesentium.<time>25 Jan 2014</time></div>
</aside>

<footer class="abs site-footer">
  <nav class="abs footer-nav"><span>Home</span><span>Who We Are</span><span>What We Offer</span><span>Support</span><span>Contact Us</span></nav>
  <div class="abs copyright">© 2013 Harlow Equipments. All Right Reserved.<br>Privacy Policy.</div>
  <div class="abs follow">Follow Us</div>
  <div class="abs socials"><span></span><span></span><span></span><span></span><span></span></div>
</footer>

</body>
</html>
```